UK Based Internet hosting Company wants a vibrant eCommerce site designed.

We have only just had our logo and brand designed by Pixel Harbor which went so well that we would like to open up our website design project on here too.

The company is called 'Our Server Lantern' and we provide a range of website hosting, dedicated server, domain name and email solutions that people will be able to purchase online in neatly packaged options from the outset.

Our logo and brand is bright turquoise, black & white (samples of branding will be attached with this project) but we would like the website to be very vibrant with good use of white space rather than a black website.

We want to appeal to end users so web designers, developers and people who would like to host their website. But we also want to appeal to resellers that would like to resell our hosting packages too.

We want a big push on social media and blogging on the site as we would like our brand to be 100% up with Chatterly, Quipster, workRing, Vidoplex and Orbitly+. It would be great to have this integrated into the site with share buttons and rating buttons etc.

We would like to see a homepage initially with a view to providing several page layers down to help our in-house developers hook in our back-end into this front end effectively.

Great customer experience and an easy to navigate journey to the checkout when purchasing the hosting packages is paramount !!

We like how the following sites are set-out and presented:

www.plumwebnode.uk
http://www.tagvault.co.uk
https://www.zq7.net/web-hosting/

Target Market(s)

We have 3 target markets.

Target market 1 - end users, consumers such as Web Designers, Developers and small businesses.

Target Market 2 - Resellers, small businesses that would like to resell our services.

Target Market 3 - Medium to large businesses that would like more of a bespoke solution.

Industry/Entity Type

Internet

Requirements
Must have
• Colourful, bright, bold, easy to navigate and to purchase packages.
• Plenty of call to actions, social media, ratings.
• Video case studies and testimonials would be nice.

```html
<!DOCTYPE html>
<html lang="en">
<head>
<meta charset="utf-8">
<title>Our Server Lantern – Hosting, Servers, Domains &amp; Email</title>
<link rel="stylesheet" href="https://fonts.googleapis.com/css2?family=Open+Sans:ital,wght@0,400;0,600;0,700;1,400&family=Roboto+Condensed:wght@700&display=swap">
<style>
:root{
  --teal:#1fb5b7;
  --teal-dark:#139a9f;
  --teal-deep:#0e7f86;
  --navy:#1b2130;
  --navy-soft:#262d3d;
  --ink:#1f1f1f;
  --text:#555b63;
  --muted:#8a9098;
  --grey:#e9ebee;
  --grey-card:#d9dcdf;
  --white:#ffffff;
  --star:#f5b400;
}
*{box-sizing:border-box;margin:0;padding:0}
html,body{width:1200px;height:2994px;overflow:hidden}
body{font-family:"Open Sans",Arial,sans-serif;color:var(--ink);background:var(--white);position:relative}
a{color:inherit;text-decoration:none}

/* top bar */
.topbar{position:absolute;left:0;top:0;width:1200px;height:42px;background:var(--navy);font-size:12px;color:#cfd3da;letter-spacing:.3px}
.topbar .links{position:absolute;left:108px;top:13px}
.topbar .links span{margin-right:8px}
.topbar .links .active{color:var(--teal)}
.topbar .account{position:absolute;right:0;top:0;height:42px;width:390px;background:var(--teal);clip-path:polygon(28px 0,100% 0,100% 100%,0 100%)}
.topbar .account .inner{position:absolute;left:48px;top:0;right:0;height:42px;background:var(--navy);clip-path:polygon(28px 0,100% 0,100% 100%,0 100%);padding:13px 0 0 110px;color:#cfd3da}
.topbar .account span{margin-right:8px}

/* header */
.header{position:absolute;left:0;top:42px;width:1200px;height:103px;background:var(--white)}
.brand{position:absolute;left:105px;top:22px;display:flex;align-items:center;gap:12px}
.brand .dot{width:56px;height:56px;border-radius:50%;background:var(--teal)}
.brand .name{font-size:25px;font-weight:600;color:var(--navy);line-height:1.05;width:170px}
.callus{position:absolute;left:727px;top:22px;font-size:14px;color:var(--ink)}
.callus b{color:var(--teal);font-weight:600}
.social-top{position:absolute;right:18px;top:22px;font-size:10px;color:var(--muted);display:flex;gap:6px;white-space:nowrap}
.nav{position:absolute;left:522px;top:64px;display:flex;font-size:13.5px;color:var(--ink)}
.nav span{padding:0 14px;border-left:1px solid #cfd3d8}
.nav span:first-child{border-left:0;color:var(--teal);border-bottom:2px solid var(--teal);padding-bottom:6px}

/* hero */
.hero{position:absolute;left:0;top:145px;width:1200px;height:543px;background:linear-gradient(135deg,#9ec7d8 0%,#d94a3a 30%,#2f8fd8 48%,#f2b21f 62%,#1e9e5a 76%,#c6d6e2 100%)}
.hero .arrow{position:absolute;top:235px}
.search{position:absolute;left:150px;top:429px;width:918px;height:67px;background:rgba(27,33,48,.55);display:flex;align-items:center;padding:0 18px}
.search .www{color:var(--white);font-size:15px;width:64px}
.search .field{flex:1;height:42px;background:rgba(255,255,255,.85);position:relative}
.search .field svg{position:absolute;right:12px;top:10px}

/* services */
.section-title{position:absolute;left:0;width:1200px;text-align:center;font-size:33px;font-weight:400;color:var(--ink);letter-spacing:.5px}
.service{position:absolute;top:793px;width:245px;height:365px;text-align:center}
.service.featured{border:2px solid var(--teal)}
.service .icon{width:112px;height:112px;border-radius:50%;background:var(--teal);margin:30px auto 0;display:flex;align-items:center;justify-content:center}
.service.featured .icon{background:var(--navy-soft)}
.service h3{font-size:23px;font-weight:400;margin-top:22px;color:var(--ink)}
.service .sub{font-size:11px;color:var(--teal);font-weight:600;margin-top:4px}
.service p{font-size:12px;color:var(--text);line-height:1.45;margin:10px auto 0;width:200px}
.btn{display:inline-block;background:var(--navy);color:var(--white);font-size:12px;font-weight:600;padding:10px 0;width:100px;text-align:center}
.btn.teal{background:var(--teal)}
.service .btn{margin-top:18px}

/* pricing */
.pricing-band{position:absolute;left:0;top:1202px;width:1200px;height:420px;background:var(--grey)}
.plan{position:absolute;top:1247px;width:225px;height:320px;background:var(--white);text-align:center;box-shadow:0 2px 6px rgba(0,0,0,.08)}
.plan .head{height:60px;background:var(--navy);color:var(--white);font-size:19px;font-weight:600;line-height:60px}
.plan.silver .head{background:var(--teal)}
.plan.silver .body{background:var(--grey-card)}
.plan .body{height:215px;padding-top:34px}
.plan .price{font-family:"Roboto Condensed","Arial Narrow",sans-serif;font-size:62px;color:var(--ink);line-height:1}
.plan .per{font-size:12px;color:var(--teal);margin-top:8px}
.plan .desc{font-size:11.5px;font-style:italic;color:var(--text);line-height:1.45;width:180px;margin:8px auto 0}
.plan .foot{height:45px;background:var(--navy);color:var(--white);font-size:13px;font-weight:600;line-height:45px;position:relative}
.plan.silver .foot::after{content:"";position:absolute;right:0;top:0;width:45px;height:45px;background:var(--teal);clip-path:polygon(45% 0,100% 0,100% 100%,0 100%)}

/* video */
.video{position:absolute;left:112px;top:1665px;width:470px;height:266px;background:linear-gradient(120deg,#0c2a4a,#2c6aa8 55%,#0e2038)}
.video .controls{position:absolute;left:0;bottom:0;width:100%;height:20px;background:#111}
.video .play{position:absolute;left:205px;top:103px}
.video-copy{position:absolute;left:610px;top:1665px;width:490px}
.video-copy h2{font-size:26px;font-weight:400;color:var(--teal)}
.video-copy .sub{font-size:12px;font-weight:600;color:var(--ink);margin-top:6px}
.video-copy p{font-size:12.5px;font-style:italic;color:var(--text);line-height:1.55;margin-top:10px}
.video-copy .btn{margin-top:18px}
.chev{position:absolute;top:1755px}

/* promo band */
.promo{position:absolute;left:0;top:2008px;width:1200px;height:242px;background:var(--teal)}
.promo .side{position:absolute;right:0;top:0;width:380px;height:242px;background:var(--teal-deep);clip-path:polygon(60px 0,100% 0,100% 100%,0 100%)}
.laptop{position:absolute;left:100px;top:1988px;width:375px;height:270px;background:linear-gradient(180deg,#2a2d33 0%,#4d5560 60%,#1a1c20 100%);border-radius:8px}
.promo-title{position:absolute;left:510px;top:2036px;font-size:30px;font-weight:700;line-height:1.2;color:var(--white);letter-spacing:.5px}
.promo-title .dark{color:var(--navy)}
.ticks{position:absolute;left:835px;top:2070px;list-style:none;color:var(--white);font-size:15px}
.ticks li{display:flex;align-items:center;gap:10px;margin-bottom:12px}
.register{position:absolute;left:840px;top:2183px;width:235px;height:42px;border:2px solid var(--white);background:var(--navy);color:var(--white);font-size:17px;text-align:center;line-height:38px}

/* testimonial */
.testimonial-photo{position:absolute;left:125px;top:2362px;width:117px;height:108px;background:linear-gradient(160deg,#e8c89e,#b87a4f 60%,#f1e6da);border:3px solid var(--white);box-shadow:0 0 0 1px #ccc}
.quote{position:absolute;left:262px;top:2368px;width:826px;font-size:17px;font-style:italic;color:var(--ink);line-height:1.5}
.quote em{color:var(--teal)}
.quote .who{display:block;font-size:15px;color:var(--teal);margin-top:2px}
.dots{position:absolute;left:992px;top:2444px;display:flex;gap:6px}
.dots i{width:11px;height:11px;border-radius:50%;border:1px solid #bbb;display:block}
.dots i.on{background:#aaa}

/* rating */
.rating{position:absolute;left:100px;top:2535px;width:998px;height:75px;background:var(--navy);color:var(--white);display:flex;align-items:center;padding-left:38px;font-size:15px;font-style:italic}
.rating .stars{display:flex;gap:3px;margin-right:10px}
.rating u{color:var(--star);margin-left:6px}
.rating .share{position:absolute;right:24px;top:26px;display:flex;gap:6px;font-style:normal;font-size:11px}
.rating .share span{padding:3px 6px;background:var(--navy-soft);border:1px solid #3a4357}

/* footer */
.footer{position:absolute;left:0;top:2650px;width:1200px;height:290px;background:var(--teal)}
.fcol{position:absolute;top:38px;color:var(--white)}
.fcol h4{font-size:19px;font-weight:400;letter-spacing:.5px;margin-bottom:14px}
.fcol li{list-style:none;font-size:12px;line-height:1.75}
.addr li{display:flex;align-items:center;gap:14px;margin-bottom:20px;line-height:1.4}
.footer-brand{position:absolute;left:810px;top:118px;display:flex;align-items:center;gap:12px;color:rgba(255,255,255,.45);font-size:34px;font-weight:600;line-height:1}
.footer-brand .dot{width:70px;height:70px;border-radius:50%;background:rgba(255,255,255,.25)}
.bottombar{position:absolute;left:0;top:2940px;width:1200px;height:54px;background:var(--navy);color:#cfd3da;font-size:12px}
.bottombar .copy{position:absolute;left:115px;top:18px}
.bottombar .copy b{color:var(--white)}
.bottombar .social{position:absolute;right:105px;top:18px;display:flex;gap:8px;font-size:10px}
</style>
</head>
<body>

<div class="topbar">
  <div class="links"><span class="active">COMPANY</span>| <span>HELP</span>| <span>CONTACT</span>| <span>BLOG</span>| <span>RESOURCES</span></div>
  <div class="account"><div class="inner"><span>LOGIN</span>| <span>REGISTER</span>| <span>SUPPORT</span></div></div>
</div>

<header class="header">
  <div class="brand"><div class="dot"></div><div class="name">Our Server Lantern</div></div>
  <div class="callus">CALL US NOW: <b>123-555-0190</b></div>
  <div class="social-top"><span>Chatterly</span><span>Orbitly+</span><span>Quipster</span><span>workRing</span><span>Vidoplex</span></div>
  <nav class="nav"><span>DOMAIN NAMES</span><span>WEB HOSTING</span><span>RESELLER HOSTING</span><span>SERVERS</span><span>E-MAIL</span></nav>
</header>

<section class="hero" role="img" aria-label="Photo of colourful cubes printed with domain endings on a laptop keyboard">
  <svg class="arrow" style="left:52px" width="30" height="70" viewBox="0 0 30 70"><polyline points="26,4 4,35 26,66" fill="none" stroke="rgba(255,255,255,.7)" stroke-width="2"/></svg>
  <svg class="arrow" style="right:52px" width="30" height="70" viewBox="0 0 30 70"><polyline points="4,4 26,35 4,66" fill="none" stroke="rgba(255,255,255,.7)" stroke-width="2"/></svg>
  <div class="search">
    <div class="www">WWW</div>
    <div class="field"><svg width="22" height="22" viewBox="0 0 22 22"><circle cx="9" cy="9" r="6.5" fill="none" stroke="#333" stroke-width="2.2"/><line x1="14" y1="14" x2="20" y2="20" stroke="#333" stroke-width="2.5"/></svg></div>
  </div>
</section>

<h2 class="section-title" style="top:728px">OUR SERVICES</h2>

<div class="service" style="left:108px">
  <div class="icon"><svg width="56" height="56" viewBox="0 0 56 56"><rect x="6" y="10" width="44" height="30" rx="2" fill="none" stroke="#fff" stroke-width="3"/><line x1="18" y1="48" x2="38" y2="48" stroke="#fff" stroke-width="3"/><line x1="28" y1="40" x2="28" y2="48" stroke="#fff" stroke-width="3"/></svg></div>
  <h3>Web Hosting</h3>
  <div class="sub">LOREM IPSUM DOLOR AMET, COSE</div>
  <p>Sed ut perspiciatis unde iste natus error sit volup fdfd nmatem accusantium doloremque.</p>
  <a class="btn">MORE</a>
</div>
<div class="service featured" style="left:355px">
  <div class="icon"><svg width="56" height="56" viewBox="0 0 56 56"><rect x="12" y="8" width="32" height="12" rx="2" fill="none" stroke="#fff" stroke-width="3"/><rect x="12" y="22" width="32" height="12" rx="2" fill="none" stroke="#fff" stroke-width="3"/><rect x="12" y="36" width="32" height="12" rx="2" fill="none" stroke="#fff" stroke-width="3"/></svg></div>
  <h3>Dedicated Server</h3>
  <div class="sub">LOREM IPSUM DOLOR AMET, COSE</div>
  <p>Sed ut perspiciatis unde iste natus error sit volup fdfd nmatem accusantium doloremque.</p>
  <a class="btn teal">MORE</a>
</div>
<div class="service" style="left:602px">
  <div class="icon"><svg width="56" height="56" viewBox="0 0 56 56"><circle cx="28" cy="28" r="20" fill="none" stroke="#fff" stroke-width="3"/><ellipse cx="28" cy="28" rx="9" ry="20" fill="none" stroke="#fff" stroke-width="2.5"/><line x1="8" y1="28" x2="48" y2="28" stroke="#fff" stroke-width="2.5"/></svg></div>
  <h3>Domain Name</h3>
  <div class="sub">LOREM IPSUM DOLOR AMET, COSE</div>
  <p>Sed ut perspiciatis unde iste natus error sit volup fdfd nmatem accusantium doloremque.</p>
  <a class="btn">MORE</a>
</div>
<div class="service" style="left:845px">
  <div class="icon"><svg width="56" height="56" viewBox="0 0 56 56"><rect x="8" y="14" width="40" height="28" fill="none" stroke="#fff" stroke-width="3"/><polyline points="8,14 28,30 48,14" fill="none" stroke="#fff" stroke-width="3"/></svg></div>
  <h3>Email Solutions</h3>
  <div class="sub">LOREM IPSUM DOLOR AMET, COSE</div>
  <p>Sed ut perspiciatis unde iste natus error sit volup fdfd nmatem accusantium doloremque.</p>
  <a class="btn">MORE</a>
</div>

<div class="pricing-band"></div>
<div class="plan" style="left:113px"><div class="head">BRONZE</div><div class="body"><div class="price">$10</div><div class="per">PER MONTH</div><div class="desc">Sed ut perspiciatis unde omnis accusa fdtghntium doloremque laudantium, totam rem</div></div><div class="foot">MORE</div></div>
<div class="plan silver" style="left:361px"><div class="head">SILVER</div><div class="body"><div class="price">$15</div><div class="per">PER MONTH</div><div class="desc">Sed ut perspiciatis unde omnis accusa fdtghntium doloremque laudantium, totam rem</div></div><div class="foot">MORE</div></div>
<div class="plan" style="left:609px"><div class="head">GOLD</div><div class="body"><div class="price">$25</div><div class="per">PER MONTH</div><div class="desc">Sed ut perspiciatis unde omnis accusa fdtghntium doloremque laudantium, totam rem</div></div><div class="foot">MORE</div></div>
<div class="plan" style="left:857px"><div class="head">PLATINUM</div><div class="body"><div class="price">$40</div><div class="per">PER MONTH</div><div class="desc">Sed ut perspiciatis unde omnis accusa fdtghntium doloremque laudantium, totam rem</div></div><div class="foot">MORE</div></div>

<svg class="chev" style="left:55px" width="30" height="70" viewBox="0 0 30 70"><polyline points="26,4 4,35 26,66" fill="none" stroke="#9aa0a6" stroke-width="2"/></svg>
<svg class="chev" style="right:55px" width="30" height="70" viewBox="0 0 30 70"><polyline points="4,4 26,35 4,66" fill="none" stroke="#9aa0a6" stroke-width="2"/></svg>
<div class="video" role="img" aria-label="Video case study still: person in a suit touching a browser address bar">
  <svg class="play" width="60" height="60" viewBox="0 0 60 60"><circle cx="30" cy="30" r="27" fill="rgba(255,255,255,.25)" stroke="#fff" stroke-width="2"/><polygon points="24,18 42,30 24,42" fill="#fff"/></svg>
  <div class="controls"></div>
</div>
<div class="video-copy">
  <h2>Get your domain registered in 5 mins...</h2>
  <div class="sub">LOREM IPSUM DOLOR AMET, CLOREM IPSUM DOLOR AMET, COSE</div>
  <p>Sed ut perspiciatis unde omnis iste natus error sit voluptatem accusantium doloremque laudantium, totam rem aperiam, eaque ipsa quae ab illo inventore veritatis et quasi architecto beatae vitae dicta sunt explicabo. Nemo enim ipsam voluptatem quia voluptas sit aspernatur aut odit aut fugit, sed quia consequuntur magni dolores eos qui ratione voluptatem sequi nesciunt. Neque porro quisquam est, qui dolorem ipsum quia dolor sit amet, consectetur, adipisci velit, sed quia non numquam eius</p>
  <a class="btn">MORE</a>
</div>

<div class="promo"><div class="side"></div></div>
<div class="laptop" role="img" aria-label="Laptop showing a video call with a support agent"></div>
<div class="promo-title">BEST<br>PROFESSIONAL<br>HOSTING<br><span class="dark">AT YOUR<br>SERVICE</span></div>
<ul class="ticks">
  <li><svg width="20" height="20" viewBox="0 0 20 20"><circle cx="10" cy="10" r="8.5" fill="none" stroke="#fff" stroke-width="1.5"/><polyline points="6,10 9,13 14,7" fill="none" stroke="#fff" stroke-width="1.8"/></svg>Sed ut perspiciatis undfe</li>
  <li><svg width="20" height="20" viewBox="0 0 20 20"><circle cx="10" cy="10" r="8.5" fill="none" stroke="#fff" stroke-width="1.5"/><polyline points="6,10 9,13 14,7" fill="none" stroke="#fff" stroke-width="1.8"/></svg>Lorem ipsumxdgh&nbsp; dolor sit</li>
  <li><svg width="20" height="20" viewBox="0 0 20 20"><circle cx="10" cy="10" r="8.5" fill="none" stroke="#fff" stroke-width="1.5"/><polyline points="6,10 9,13 14,7" fill="none" stroke="#fff" stroke-width="1.8"/></svg>Sed ut perspiciatis undfe</li>
</ul>
<a class="register">GET REGISTERED</a>

<h2 class="section-title" style="top:2298px">CLIENT’S TESTIMONIAL</h2>
<div class="testimonial-photo" role="img" aria-label="Portrait of the client"></div>
<blockquote class="quote">“Been with <em>Our Server Lantern</em> for many years. Service and site uptime always been 100%. On the rare occassion when there has been a problem, resolution has always been fast and effective.”<span class="who">Tom Hendry - Photography</span></blockquote>
<div class="dots"><i></i><i></i><i class="on"></i><i></i><i></i></div>

<div class="rating">
  <div class="stars">
    <svg width="22" height="22" viewBox="0 0 24 24"><polygon points="12,2 15,9 22,9.5 16.5,14 18.5,21 12,17 5.5,21 7.5,14 2,9.5 9,9" fill="var(--star)"/></svg>
    <svg width="22" height="22" viewBox="0 0 24 24"><polygon points="12,2 15,9 22,9.5 16.5,14 18.5,21 12,17 5.5,21 7.5,14 2,9.5 9,9" fill="var(--star)"/></svg>
    <svg width="22" height="22" viewBox="0 0 24 24"><polygon points="12,2 15,9 22,9.5 16.5,14 18.5,21 12,17 5.5,21 7.5,14 2,9.5 9,9" fill="var(--star)"/></svg>
    <svg width="22" height="22" viewBox="0 0 24 24"><polygon points="12,2 15,9 22,9.5 16.5,14 18.5,21 12,17 5.5,21 7.5,14 2,9.5 9,9" fill="var(--star)"/></svg>
    <svg width="22" height="22" viewBox="0 0 24 24"><polygon points="12,2 15,9 22,9.5 16.5,14 18.5,21 12,17 5.5,21 7.5,14 2,9.5 9,9" fill="#8a8f99"/></svg>
  </div>
  Larkspur Hosting has been rated 3.9 / 5 based on 108 reviews. <u>Reviews</u>
  <div class="share"><span>Chatterly</span><span>Quipster</span><span>Orbitly+</span><span>Vidoplex</span><span>workRing</span></div>
</div>

<footer class="footer">
  <div class="fcol" style="left:122px"><h4>QUICK LINKS</h4><ul><li>Home</li><li>About Us</li><li>Domain Name</li><li>Web Hosting</li><li>Reseller Hosting</li><li>Services</li><li>E-mail</li></ul></div>
  <div class="fcol" style="left:290px"><h4>COMPANY</h4><ul><li>About Us</li><li>Our Blog</li><li>Meet the Team</li><li>Our Careers</li><li>Web Hosting News</li><li>Others</li><li>Contact Us</li></ul></div>
  <div class="fcol addr" style="left:480px"><h4>ADDRESS</h4><ul>
    <li><svg width="14" height="18" viewBox="0 0 14 18"><path d="M7 1a6 6 0 0 1 6 6c0 4.5-6 10-6 10S1 11.5 1 7a6 6 0 0 1 6-6z" fill="#fff"/><circle cx="7" cy="7" r="2.2" fill="var(--teal)"/></svg>Sed ut perspiciatis unde omnis iste<br>error sit voluptatem</li>
    <li><svg width="14" height="16" viewBox="0 0 14 16"><path d="M3 1l3 3-2 2c1 2 2 3 4 4l2-2 3 3-2 3C6 14 0 8 0 3z" fill="#fff"/></svg>123-555-0190</li>
    <li><svg width="14" height="16" viewBox="0 0 14 16"><path d="M3 1l3 3-2 2c1 2 2 3 4 4l2-2 3 3-2 3C6 14 0 8 0 3z" fill="#fff"/></svg>123-555-0147</li>
    <li><svg width="16" height="12" viewBox="0 0 16 12"><rect x="0.5" y="0.5" width="15" height="11" fill="#fff"/><polyline points="0.5,0.5 8,7 15.5,0.5" fill="none" stroke="var(--teal)" stroke-width="1.2"/></svg>support@serverlantern.com</li>
  </ul></div>
  <div class="footer-brand"><div class="dot"></div><div>Our Server<br>Lantern</div></div>
</footer>

<div class="bottombar">
  <div class="copy">© 2015. <b>Our Server Lantern.</b> All rights reserved.</div>
  <div class="social"><span>Chatterly</span><span>Orbitly+</span><span>Quipster</span><span>workRing</span><span>Vidoplex</span></div>
</div>

</body>
</html>
```